Holiday Rental Company Flyer Design (DL not A5)

Project Brief:
We need a double sided DL flyer designed for an up market Holiday Rental Company that portrays a personalised approach to property management. These are to be used for letter box drops to homes we're specifically targeting so the design should be modern, complimentary colour palette, uncluttered & visually appealing.

Please Download the DL Template from Quillmark here: http://www.quillmark-example.com.au/vp/ns/propath/UploadResources.aspx?selectedTab=0?pfid=BFB&pf_id=BFB&xnav=easypath-upload-image#Templates

Target Market(s)

Wealthy Home Owners

Industry/Entity Type

It Company

Font styles to use
Other font styles liked:
• Avant Garde Extra Light & Demi

Colors
33b8a4

Requirements
Must have
• DL Flyer sizes (210mm width x 99mm width, plus 3mm bleed)
• Front: Logo, Main Image & Grab
• Back: Contact Details & Brief Description of our business
• Images: Ideally the main image should be the house with the pool but alternatively a lifestyle images could also be used.
Nice to have
• A creative designer!
Should not have
• Clutter & busy designs

```html
<!DOCTYPE html>
<html lang="en">
<head>
<meta charset="utf-8">
<title>Coastal Stays – DL Flyer</title>
<link rel="stylesheet" href="https://fonts.googleapis.com/css2?family=Poppins:wght@200;300;400;500;600&display=swap">
<style>
  :root{
    --page:#ece9e4;
    --slate:#3d4145;
    --slate-dark:#2b2e31;
    --mint:#55e59c;
    --mint-deep:#3fd68a;
    --ink:#1f2224;
    --text:#2e3134;
    --white:#ffffff;
    --tick:#d3262b;
  }
  *{box-sizing:border-box;margin:0;padding:0}
  html,body{width:1200px;height:1056px;overflow:hidden}
  body{background:var(--page);font-family:"Poppins",sans-serif;position:relative}

  .flyer{position:absolute;width:468px;overflow:hidden;box-shadow:0 2px 8px rgba(0,0,0,.15)}

  /* Front */
  .flyer--front{left:68px;top:45px;height:968px;background:var(--slate)}
  .front__grab{position:absolute;top:62px;width:100%;text-align:center;line-height:1.2}
  .front__grab-title{color:var(--mint);font-weight:600;font-size:27px;letter-spacing:-.2px}
  .front__grab-sub{color:var(--white);font-weight:300;font-size:26px;letter-spacing:-.3px}
  .front__name{position:absolute;top:205px;width:100%;text-align:center;color:var(--white);
    font-weight:200;font-size:58px;line-height:62px;letter-spacing:6px}
  .front__mark{position:absolute;left:210px;top:350px;width:48px;height:48px;border:2px solid var(--mint);border-radius:50%}
  .front__photo{position:absolute;left:0;top:420px;width:100%;height:548px;
    background:linear-gradient(180deg,#3d4145 0%,#2c2f6a 30%,#3a3aa8 55%,#8a7a6a 75%,#3f8fe0 90%,#69b8ff 100%)}

  /* Back */
  .flyer--back{left:660px;top:45px;height:973px;background:var(--white)}
  .back__photo{position:absolute;left:0;top:0;width:100%;height:200px;
    background:linear-gradient(135deg,#8b8480 0%,#a39a92 45%,#6f7a52 70%,#c8643a 100%)}
  .back__intro{position:absolute;left:0;top:198px;width:100%;height:162px;background:var(--mint);
    border-bottom:7px solid var(--slate-dark)}
  .back__intro-rule{position:absolute;left:40px;top:22px;width:3px;height:112px;background:var(--white)}
  .back__intro-title{position:absolute;left:58px;top:30px;font-size:27px;font-weight:500;color:var(--white);letter-spacing:-.3px}
  .back__intro-title strong{color:var(--ink);font-weight:600}
  .back__intro-text{position:absolute;left:60px;top:74px;width:370px;font-size:14.2px;line-height:19.5px;
    color:var(--white);font-weight:300;text-align:justify}

  .service__photo{position:absolute;left:23px;top:380px;width:175px;height:121px;
    background:linear-gradient(135deg,#c9a88a 0%,#e3d3b8 40%,#c7cf3a 65%,#e05a3a 100%);
    clip-path:polygon(0 0,100% 0,100% 88%,95% 100%,0 100%)}
  .service__edge{position:absolute;left:186px;top:380px;width:18px;height:121px;background:var(--mint);
    clip-path:polygon(70% 0,100% 0,35% 100%,0 100%)}
  .service__title{position:absolute;left:209px;top:391px;font-size:21px;line-height:27px;font-weight:600;color:var(--mint-deep)}
  .service__title strong{color:var(--ink);font-weight:600}
  .service__text{position:absolute;left:209px;top:447px;width:222px;font-size:15px;line-height:19.5px;
    color:var(--text);font-weight:300;text-align:justify;text-align-last:left}

  .benefits{position:absolute;left:38px;top:548px;width:395px;list-style:none}
  .benefit{position:relative;height:72px;padding-left:55px;font-size:14px;letter-spacing:-.3px;line-height:19.5px;color:var(--text);font-weight:300;text-align:justify}
  .benefit svg{position:absolute;left:0;top:-6px}

  .cta{position:absolute;left:0;top:745px;width:100%;height:120px;background:var(--slate-dark)}
  .cta__band{position:absolute;left:0;top:0;width:400px;height:120px;background:var(--mint);
    clip-path:polygon(0 0,375px 0,400px 120px,0 120px)}
  .cta__text{position:absolute;left:0;top:10px;width:400px;text-align:center;color:var(--white);
    font-size:17.5px;line-height:23px;font-weight:400}
  .cta__text strong{display:block;color:var(--ink);font-weight:600;font-size:20px;margin-top:3px}

  .contacts{position:absolute;left:28px;top:883px;width:420px;font-size:13px;color:var(--text);font-weight:400}
  .contact{position:absolute;display:flex;align-items:center;gap:6px;white-space:nowrap}
  .contact--left{left:0}
  .contact--right{left:188px}
  .contact--row1{top:0}
  .contact--row2{top:30px}
  .contact__icon{width:21px;height:21px;border-radius:50%;background:var(--slate);display:flex;align-items:center;justify-content:center;flex:none}
</style>
</head>
<body>

<section class="flyer flyer--front">
  <div class="front__grab">
    <div class="front__grab-title">Holiday Rental Management</div>
    <div class="front__grab-sub">with a difference</div>
  </div>
  <h1 class="front__name">COASTAL<br>STAYS</h1>
  <div class="front__mark" aria-hidden="true"></div>
  <div class="front__photo" role="img" aria-label="Night photograph of a modern house with a lit courtyard and blue swimming pool"></div>
</section>

<section class="flyer flyer--back">
  <div class="back__photo" role="img" aria-label="Photograph of orange bird of paradise flowers against a stone tiled wall"></div>

  <div class="back__intro">
    <span class="back__intro-rule"></span>
    <h2 class="back__intro-title">What we do <strong>differently!</strong></h2>
    <p class="back__intro-text">Rather than relying upon a key safe or a central pick-up destination, a ‘Coastal Stays’ staff member will greet guests upon arrival.</p>
  </div>

  <div class="service__photo" role="img" aria-label="Photograph of a bed with yellow cushions and a colourful patterned quilt"></div>
  <span class="service__edge"></span>
  <h3 class="service__title">Our ‘<strong>Meet &amp; Greet</strong>’<br>Service provides</h3>
  <p class="service__text">home owners with an increased level of Security and also allows us to:</p>

  <ul class="benefits">
    <li class="benefit">
      <svg width="40" height="40" viewBox="0 0 40 40" aria-hidden="true"><path d="M4 22 L20 16 L34 26 L18 34 Z" fill="none" stroke="#222" stroke-width="2.5"/><path d="M12 20 L18 27 L32 4" fill="none" stroke="var(--tick)" stroke-width="4" stroke-linecap="round" stroke-linejoin="round"/></svg>
      Prepare the home for their arrival (lights, heaters, music etc.)
    </li>
    <li class="benefit">
      <svg width="40" height="40" viewBox="0 0 40 40" aria-hidden="true"><path d="M4 22 L20 16 L34 26 L18 34 Z" fill="none" stroke="#222" stroke-width="2.5"/><path d="M12 20 L18 27 L32 4" fill="none" stroke="var(--tick)" stroke-width="4" stroke-linecap="round" stroke-linejoin="round"/></svg>
      Establish a rapport &amp; help facilitate future bookings
    </li>
    <li class="benefit">
      <svg width="40" height="40" viewBox="0 0 40 40" aria-hidden="true"><path d="M4 22 L20 16 L34 26 L18 34 Z" fill="none" stroke="#222" stroke-width="2.5"/><path d="M12 20 L18 27 L32 4" fill="none" stroke="var(--tick)" stroke-width="4" stroke-linecap="round" stroke-linejoin="round"/></svg>
      Reiterate their responsibilities to ensure the return of their bond
    </li>
  </ul>

  <div class="cta">
    <div class="cta__band"></div>
    <p class="cta__text">If you’d like to know what your<br>property could achieve or require<br>additional information.<strong>Please contact us on</strong></p>
  </div>

  <div class="contacts">
    <div class="contact contact--left contact--row1">
      <span class="contact__icon"><svg width="12" height="12" viewBox="0 0 24 24"><path d="M6.6 10.8a15 15 0 0 0 6.6 6.6l2.2-2.2a1 1 0 0 1 1-.25 11 11 0 0 0 3.6.6 1 1 0 0 1 1 1V20a1 1 0 0 1-1 1A17 17 0 0 1 3 4a1 1 0 0 1 1-1h3.5a1 1 0 0 1 1 1 11 11 0 0 0 .6 3.6 1 1 0 0 1-.25 1z" fill="#fff"/></svg></span>
      (03)5550 1234
    </div>
    <div class="contact contact--right contact--row1">
      <span class="contact__icon"><svg width="12" height="12" viewBox="0 0 24 24"><rect x="3" y="6" width="18" height="12" rx="1" fill="none" stroke="#fff" stroke-width="2"/><path d="M3 7l9 6 9-6" fill="none" stroke="#fff" stroke-width="2"/></svg></span>
      stay@coastalstays.com.au
    </div>
    <div class="contact contact--left contact--row2">
      <span class="contact__icon"><svg width="13" height="13" viewBox="0 0 24 24"><circle cx="12" cy="12" r="9" fill="none" stroke="#fff" stroke-width="2"/><path d="M3 12h18M12 3c3 3 3 15 0 18M12 3c-3 3-3 15 0 18" fill="none" stroke="#fff" stroke-width="1.6"/></svg></span>
      coastalstays.com.au
    </div>
    <div class="contact contact--right contact--row2">
      <span class="contact__icon"><svg width="12" height="12" viewBox="0 0 24 24"><path d="M12 2a7 7 0 0 0-7 7c0 5 7 13 7 13s7-8 7-13a7 7 0 0 0-7-7zm0 9.5A2.5 2.5 0 1 1 12 6.5a2.5 2.5 0 0 1 0 5z" fill="#fff"/></svg></span>
      PO Box 12, Seaview Victoria 3999
    </div>
  </div>
</section>

</body>
</html>
```